Business Card for Veltrano, a french tech company

Tech company
New technologies
Serious design
Dark theme

User info :
Name: Mathis CORLAVE
Position: Co-Founder & CEO
Tel: (+33) 6 58 24 90 37
Email: mathis@veltrano.io
Website: www.veltrano.io
Address: 17 rue des Tanneurs 69002 LYON

Attached is the business logo file.

```html
<!DOCTYPE html>
<html lang="en">
<head>
<meta charset="UTF-8">
<title>Veltrano – Business Card</title>
<link rel="stylesheet" href="https://fonts.googleapis.com/css2?family=Poppins:wght@400;500;600&display=swap">
<style>
  :root {
    --backdrop: #6a6a6a;
    --card: #000000;
    --magenta: #e6009e;
    --violet: #a000e0;
    --brand: #b800d0;
    --ink: #ffffff;
  }
  * { margin: 0; padding: 0; box-sizing: border-box; }
  html, body {
    width: 1093px; height: 1200px; overflow: hidden;
    background: var(--backdrop);
    font-family: "Poppins", sans-serif;
  }
  .card {
    position: absolute;
    left: 265px;
    width: 582px;
    height: 358px;
    background: var(--card);
    border-radius: 28px;
    box-shadow: 0 4px 8px rgba(0,0,0,.35);
  }
  .card--front { top: 226px; }
  .card--back { top: 621px; }

  .holder { position: absolute; left: 26px; top: 60px; }
  .holder__name {
    font-weight: 600; font-size: 24px; line-height: 1;
    text-transform: uppercase;
    background: linear-gradient(90deg, var(--magenta), var(--violet));
    -webkit-background-clip: text; background-clip: text; color: transparent;
    letter-spacing: .2px;
  }
  .holder__role {
    color: var(--ink); font-size: 17px; line-height: 1; margin-top: 2px;
  }
  .rule {
    position: absolute; left: 29px; width: 61px; height: 1px;
    background: var(--magenta);
  }
  .rule--upper { top: 122px; }
  .rule--lower { top: 230px; }

  .contacts {
    position: absolute; left: 26px; top: 146px;
    list-style: none; color: var(--ink); font-size: 17.5px; line-height: 21px;
  }
  .contacts li { display: flex; align-items: center; gap: 7px; white-space: nowrap; }
  .contacts svg { width: 16px; height: 16px; flex: none; }

  .address {
    position: absolute; left: 27px; top: 250px;
    color: var(--ink); font-size: 17.5px; line-height: 21px;
  }

  .brand-name {
    position: absolute; font-weight: 600; color: var(--brand);
    letter-spacing: 1px; line-height: 1;
  }
  .card--front .brand-name {
    left: 300px; width: 232px; top: 157px; text-align: center; font-size: 40px;
  }
  .card--back .brand-name {
    left: 0; width: 100%; top: 146px; text-align: center; font-size: 62px; letter-spacing: 2px;
  }
</style>
</head>
<body>
  <section class="card card--front">
    <div class="holder">
      <h1 class="holder__name">Mathis Corlave</h1>
      <p class="holder__role">Co-Founder &amp; CEO</p>
    </div>
    <span class="rule rule--upper"></span>
    <ul class="contacts">
      <li>
        <svg viewBox="0 0 16 16" fill="none" stroke="var(--magenta)" stroke-width="1.6" stroke-linecap="round">
          <path d="M3 2l3 1 1 3-2 1.5a9 9 0 0 0 3.5 3.5L10 9l3 1 1 3-2 1.5C7 14 2 9 1.5 4z"/>
          <path d="M10 2a4 4 0 0 1 4 4M10 4.5a1.6 1.6 0 0 1 1.5 1.5"/>
        </svg>
        (+33) 6 58 24 90 37
      </li>
      <li>
        <svg viewBox="0 0 16 16" fill="none" stroke="var(--magenta)" stroke-width="1.6">
          <rect x="0.8" y="3" width="14.4" height="10" fill="var(--magenta)" stroke="none"/>
          <path d="M1 3.5l7 5.5 7-5.5M1 12.5l5-4.5M15 12.5l-5-4.5" stroke="#000" stroke-width="1.2"/>
        </svg>
        mathis@veltrano.io
      </li>
      <li>
        <svg viewBox="0 0 16 16" fill="none" stroke="var(--magenta)" stroke-width="1.3">
          <circle cx="8" cy="8" r="6.8"/>
          <ellipse cx="8" cy="8" rx="3" ry="6.8"/>
          <path d="M1.2 8h13.6M2.2 4.5h11.6M2.2 11.5h11.6M8 1.2v13.6"/>
        </svg>
        www.veltrano.io
      </li>
    </ul>
    <span class="rule rule--lower"></span>
    <p class="address">17 rue des Tanneurs<br>69002 LYON</p>
    <span class="brand-name">VELTRANO</span>
  </section>

  <section class="card card--back">
    <span class="brand-name">VELTRANO</span>
  </section>
</body>
</html>
```